Business Card Design

I need a business card for my company i am starting. I will be providing stump grinding services. I use a motorized machine to grind stumps down under the ground so that they are out of the way and out of sight. I'm looking for my card to have maroon or dark red somewhere in the card to match my truck. I'm going to use this card to advertise and also serve as a design to wrap my truck tailgate as advertisement so i want it to match. the dark maroon color of my truck. I wouldn't mind using bright colors or color for the rest of the card or the lettering or any designs on the card. In the images i have provided i like how there are saw blades integrated into these people advertisements. I also like the illustration of the stump grinder. I also provided a picture of the actual cutting wheel or blade of the grinder.

Industry/Entity Type

Business

Contact Information for Business Card

Company Name - Oakline Stump Grinding
Phone - 407-219-5573
Email - harlow.stumpwork@quillpost.net
Name and title - Thomas Harlow - Owner and operator
Company Slogan - Roots out, level ground for you

```html
<!DOCTYPE html>
<html lang="en">
<head>
<meta charset="utf-8">
<title>Oakline Stump Grinding – Business Card</title>
<link href="https://fonts.googleapis.com/css2?family=Ubuntu:wght@400;500;700&display=swap" rel="stylesheet">
<style>
  :root {
    --backdrop: #e9e6e1;
    --card-white: #f7f7f7;
    --card-shade: #e4e4e4;
    --maroon: #a8131d;
    --maroon-deep: #8c0f18;
    --maroon-light: #c03a42;
    --on-maroon: #ffffff;
  }
  * { margin: 0; padding: 0; box-sizing: border-box; }
  html, body {
    width: 1200px; height: 780px; overflow: hidden;
    background: var(--backdrop);
  }
  .canvas {
    position: relative; width: 1200px; height: 780px;
    display: flex; align-items: center; justify-content: center;
  }
  .business-card {
    position: relative; width: 1000px; height: 572px;
    border-radius: 22px; overflow: hidden;
    background: linear-gradient(160deg, var(--card-white) 40%, var(--card-shade) 100%);
    box-shadow: 0 14px 34px rgba(0,0,0,0.18);
    font-family: "Ubuntu", sans-serif;
  }
  .brand-block {
    position: absolute; left: 140px; top: 112px;
    display: flex; align-items: center; gap: 28px;
  }
  .brand-dot {
    width: 104px; height: 104px; border-radius: 50%;
    background: var(--maroon);
    flex: none;
  }
  .brand-text { display: flex; flex-direction: column; }
  .company-name {
    font-weight: 700; font-size: 56px; line-height: 1;
    color: var(--maroon); letter-spacing: 0.5px; white-space: nowrap;
  }
  .slogan {
    margin-top: 12px;
    font-weight: 400; font-size: 23px; letter-spacing: 5px;
    color: var(--maroon); white-space: nowrap;
  }
  .name-band {
    position: absolute; left: 0; right: 0; top: 292px; height: 96px;
    background: linear-gradient(180deg, var(--maroon-light) 0%, var(--maroon) 35%, var(--maroon-deep) 100%);
    padding: 14px 0 0 272px;
    color: var(--on-maroon);
  }
  .person-name { font-weight: 700; font-size: 36px; line-height: 1.05; }
  .person-title { font-weight: 500; font-size: 24px; line-height: 1.2; }
  .contact-list {
    position: absolute; left: 272px; top: 414px;
    list-style: none; color: var(--maroon);
  }
  .contact-phone { font-weight: 500; font-size: 30px; line-height: 1.3; }
  .contact-email { font-weight: 400; font-size: 26px; line-height: 1.4; }
</style>
</head>
<body>
<main class="canvas">
  <article class="business-card">
    <header class="brand-block">
      <div class="brand-dot" aria-hidden="true"></div>
      <div class="brand-text">
        <h1 class="company-name">Oakline Stump Grinding</h1>
        <p class="slogan">Roots out, level ground for you</p>
      </div>
    </header>
    <section class="name-band">
      <p class="person-name">Thomas Harlow</p>
      <p class="person-title">Owner and operator</p>
    </section>
    <ul class="contact-list">
      <li class="contact-phone">407-219-5573</li>
      <li class="contact-email">harlow.stumpwork@quillpost.net</li>
    </ul>
  </article>
</main>
</body>
</html>
```